Prairie Kettle Billboard

We are looking to have a new billboard design for our Casual Restaurant chain. We are a steakhouse chain that is very casual. You can visit our website at: www.prairiekettle-demo.net to get an idea of our menu. We are looking to have some new billboard ideas for our steakhouse so that we can communicate our concept to customers that are passing by the billboard. I have attached some items to give you a feel for our concept. The Billboard will be 14'X48'. I look forward to hearing from you. Glen

```html
<!DOCTYPE html>
<html lang="en">
<head>
<meta charset="utf-8">
<title>Prairie Kettle Billboard</title>
<link rel="stylesheet" href="https://fonts.googleapis.com/css2?family=Lato:wght@400;700&display=swap">
<style>
  :root {
    --page-bg: #e9ecef;
    --panel-black: #0b0b0b;
    --accent-orange: #f5a21b;
    --brand-red: #e0321c;
    --text-white: #ffffff;
    --fire-deep: #8a2a05;
    --fire-mid: #e0670f;
    --fire-bright: #ffc04a;
    --meat-dark: #4a1a0a;
    --meat-mid: #7a3214;
  }
  html, body {
    margin: 0;
    width: 1200px;
    height: 900px;
    overflow: hidden;
    background: var(--page-bg);
  }
  .billboard {
    position: absolute;
    left: 40px;
    top: 286px;
    width: 1120px;
    height: 327px;
    display: block;
  }
  .headline {
    font-family: "Lato", sans-serif;
    font-weight: 400;
    font-size: 46px;
    letter-spacing: 0.5px;
  }
  .headline-white { fill: var(--text-white); }
  .headline-orange { fill: var(--accent-orange); }
  .brand-name {
    font-family: "Lato", sans-serif;
    font-weight: 700;
    font-size: 34px;
    fill: var(--brand-red);
  }
</style>
</head>
<body>
<svg class="billboard" viewBox="0 0 1120 327" xmlns="http://www.w3.org/2000/svg">
  <defs>
    <linearGradient id="steak-photo-fire" x1="0" y1="0" x2="1" y2="1">
      <stop offset="0" stop-color="var(--fire-bright)"/>
      <stop offset="0.35" stop-color="var(--fire-mid)"/>
      <stop offset="0.7" stop-color="var(--fire-deep)"/>
      <stop offset="1" stop-color="var(--fire-mid)"/>
    </linearGradient>
    <radialGradient id="steak-photo-meat" cx="0.5" cy="0.58" r="0.5">
      <stop offset="0" stop-color="var(--meat-dark)" stop-opacity="0.95"/>
      <stop offset="0.6" stop-color="var(--meat-mid)" stop-opacity="0.75"/>
      <stop offset="1" stop-color="var(--meat-mid)" stop-opacity="0"/>
    </radialGradient>
    <linearGradient id="flame-tone" x1="0" y1="1" x2="0" y2="0">
      <stop offset="0" stop-color="var(--fire-mid)" stop-opacity="0.85"/>
      <stop offset="1" stop-color="var(--fire-deep)" stop-opacity="0"/>
    </linearGradient>
    <clipPath id="photo-shape">
      <polygon points="0,0 760,0 605,327 0,327"/>
    </clipPath>
    <clipPath id="black-panel-shape">
      <polygon points="778,0 1120,0 1120,327 623,327"/>
    </clipPath>
  </defs>

  <rect class="panel-black" x="0" y="0" width="1120" height="327" fill="var(--panel-black)"/>

  <g class="photo-steak" clip-path="url(#photo-shape)" role="img"
     aria-label="Close-up photo of a grilled steak over open flames">
    <rect x="0" y="0" width="760" height="327" fill="url(#steak-photo-fire)"/>
    <rect x="0" y="0" width="760" height="327" fill="url(#steak-photo-meat)"/>
  </g>

  <polygon class="divider-stripe" points="760,0 778,0 623,327 605,327" fill="var(--accent-orange)"/>

  <g clip-path="url(#black-panel-shape)">
    <rect class="flames-band" x="600" y="255" width="520" height="72"
          fill="url(#flame-tone)" role="img" aria-label="Grill flames along the bottom edge"/>
  </g>

  <text class="headline headline-white" x="1080" y="92" text-anchor="end">WELL DONE,</text>
  <text class="headline headline-orange" x="1080" y="146" text-anchor="end">STEAK.</text>

  <circle class="brand-dot" cx="793" cy="225" r="9" fill="var(--brand-red)"/>
  <text class="brand-name" x="813" y="237">Prairie Kettle</text>
</svg>
</body>
</html>
```